Healthcare technology firm needs business card layout. Logo provided.

We need a business card design for a new healthcare technology company called Mirvela.com. The logo is already done so that will be used in the design. We assist patients and their families manage their personal health finances. Our initial product is our web site membership that includes educational content on your health benefits, tools, and downloadable forms.

We would like to see designs that use our existing logo or extend the logo in a creative way. Should be very consumer friendly.

```html
<!DOCTYPE html>
<html lang="en">
<head>
<meta charset="utf-8">
<title>Mirvela Business Card</title>
<link rel="stylesheet" href="https://fonts.googleapis.com/css2?family=Jost:wght@400;500;600&display=swap">
<style>
  :root {
    --backdrop: #8a8a86;
    --blue-deep: #0b4ea6;
    --blue-bright: #0a86d2;
    --blue-logo: #0f5bb5;
    --card-white: #f4f6f7;
    --text-light: #e9f1fa;
    --divider: rgba(255, 255, 255, 0.55);
  }
  * { box-sizing: border-box; margin: 0; padding: 0; }
  html, body {
    width: 1200px;
    height: 774px;
    overflow: hidden;
  }
  body {
    background: var(--backdrop);
    font-family: "Jost", "Futura", sans-serif;
    display: flex;
    align-items: center;
    justify-content: center;
    gap: 40px;
  }
  .card {
    width: 540px;
    height: 309px;
    border-radius: 4px;
    position: relative;
    overflow: hidden;
    box-shadow: 0 10px 30px rgba(0, 0, 0, 0.25);
  }

  /* Front: contact side */
  .card--front {
    background: linear-gradient(100deg, var(--blue-deep) 0%, var(--blue-bright) 100%);
    color: var(--text-light);
  }
  .front-logo {
    position: absolute;
    left: 48px;
    top: 136px;
    display: flex;
    align-items: center;
    gap: 8px;
  }
  .front-logo__name {
    font-size: 32px;
    font-weight: 500;
    letter-spacing: 1px;
    color: var(--text-light);
  }
  .front-logo__dot {
    width: 9px;
    height: 9px;
    border-radius: 50%;
    background: var(--text-light);
  }
  .front-divider {
    position: absolute;
    left: 248px;
    top: 40px;
    width: 1px;
    height: 160px;
    background: var(--divider);
  }
  .contact {
    position: absolute;
    left: 272px;
    top: 42px;
    right: 20px;
    line-height: 1.25;
  }
  .contact__name { font-size: 20px; font-weight: 600; }
  .contact__title { font-size: 15px; font-weight: 400; margin-bottom: 20px; }
  .contact__phone { font-size: 16px; margin-bottom: 18px; }
  .contact__tagline { font-size: 15px; }
  .contact__web { font-size: 15px; }
  .contact__web strong { font-weight: 600; }

  /* Back: brand side */
  .card--back {
    background: var(--card-white);
  }
  .back-logo {
    position: absolute;
    left: 0;
    right: 0;
    top: 78px;
    display: flex;
    justify-content: center;
    align-items: center;
    gap: 12px;
  }
  .back-logo__name {
    font-size: 76px;
    font-weight: 500;
    letter-spacing: 2px;
    color: var(--blue-logo);
  }
  .back-logo__dot {
    width: 18px;
    height: 18px;
    border-radius: 50%;
    background: var(--blue-logo);
    margin-top: 30px;
  }
  .locations {
    position: absolute;
    left: 0;
    right: 18px;
    bottom: 0;
    height: 52px;
    background: linear-gradient(90deg, var(--blue-deep), var(--blue-bright));
    border-top-right-radius: 26px;
    display: flex;
    align-items: center;
    padding-left: 28px;
    gap: 12px;
    color: var(--text-light);
    font-size: 18px;
    list-style: none;
    white-space: nowrap;
  }
  .locations li + li::before {
    content: "";
    display: inline-block;
    width: 6px;
    height: 6px;
    border-radius: 50%;
    background: var(--text-light);
    margin-right: 12px;
    vertical-align: middle;
  }
</style>
</head>
<body>
  <section class="card card--front" aria-label="Business card front">
    <div class="front-logo">
      <span class="front-logo__name">MIRVELA</span>
      <span class="front-logo__dot"></span>
    </div>
    <div class="front-divider"></div>
    <div class="contact">
      <p class="contact__name">Dana R. Whitfield</p>
      <p class="contact__title">CEO</p>
      <p class="contact__phone">555-014-2367</p>
      <p class="contact__tagline">Clarity for every care expense</p>
      <p class="contact__web">www.<strong>mirvela</strong>.com</p>
    </div>
  </section>

  <section class="card card--back" aria-label="Business card back">
    <div class="back-logo">
      <span class="back-logo__name">MIRVELA</span>
      <span class="back-logo__dot"></span>
    </div>
    <ul class="locations">
      <li>Alder Point</li>
      <li>Marlow Bay</li>
      <li>Cresthaven</li>
      <li>Norvik</li>
    </ul>
  </section>
</body>
</html>
```